Boutique Sparkling Blanc de Blancs Wine label

We are looking for a label and neck label for our new Sparkling Chardonnay.
Images uploaded include, bubbles and glitter maybe as a faded background for whole label?
We like Refined, elegant yet simple designs.
Have included our current table chardonnay label as example.

Industry/Entity Type

Boutique

Font styles to use
Decorative
Script

Requirements
Must have
• Name - "Every Moonlit Hour"
• Methode Traditionelle
• Blanc de Blancs
• 2015
• Beyond the Orchards (Brand)
• Adelaide Hills
Nice to have
• Neutral tones
• Sparkles, Glitter, Bubbles
• Traditional, cursive or vine like fonts
• Have attached fonts we used for previous wine label - might be nice to carry through same/similar fonts to continue our brand?
Should not have
• a lot of colour

```html
<!DOCTYPE html>
<html lang="en">
<head>
<meta charset="utf-8">
<title>Every Moonlit Hour – Blanc de Blancs Labels</title>
<link rel="stylesheet" href="https://fonts.googleapis.com/css2?family=Great+Vibes&family=Cinzel:wght@400;500&family=Cormorant+Garamond:wght@500&display=swap">
<style>
  :root {
    --backdrop: #e4e8ee;
    --cream: #f5f0de;
    --cream-light: #fbf8ee;
    --gold: #c39d52;
    --gold-deep: #a47e36;
    --silver: #a9a9a9;
    --silver-light: #d9d9d9;
    --ink-soft: #8e8a80;
    --night: #0d0d0d;
    --night-soft: #1c1c1c;
    --pearl: #e9e6df;
  }
  html, body {
    margin: 0;
    width: 1200px;
    height: 1200px;
    overflow: hidden;
    background: var(--backdrop);
  }
  .canvas {
    position: relative;
    width: 1200px;
    height: 1200px;
    display: flex;
    justify-content: center;
    align-items: center;
    gap: 120px;
  }
  .label {
    position: relative;
    width: 460px;
    height: 400px;
    box-sizing: border-box;
    text-align: center;
    overflow: hidden;
  }
  .label--cream {
    background: radial-gradient(ellipse at 50% 40%, var(--cream-light), var(--cream));
    border-top: 10px solid var(--gold);
    border-bottom: 10px solid var(--gold);
  }
  .label--night {
    background: radial-gradient(ellipse at 50% 40%, var(--night-soft), var(--night));
    border-top: 10px solid var(--silver-light);
    border-bottom: 10px solid var(--silver-light);
  }
  .sparkle-art {
    position: absolute;
    left: 120px;
    top: 34px;
    width: 280px;
    height: 190px;
    border-radius: 50%;
  }
  .label--cream .sparkle-art {
    background: radial-gradient(ellipse at 70% 45%, rgba(150,150,150,0.28), rgba(195,157,82,0.12) 55%, transparent 72%);
  }
  .label--night .sparkle-art {
    background: radial-gradient(ellipse at 70% 45%, rgba(220,220,220,0.22), rgba(195,157,82,0.12) 55%, transparent 72%);
  }
  .product-name {
    position: relative;
    margin: 0;
    padding-top: 60px;
    font-family: "Great Vibes", cursive;
    font-weight: 400;
    line-height: 0.9;
  }
  .product-name__lead {
    display: block;
    font-size: 44px;
  }
  .product-name__main {
    display: block;
    font-size: 96px;
  }
  .label--cream .product-name { color: var(--silver); }
  .label--night .product-name { color: var(--gold); }
  .style {
    position: relative;
    margin: 4px 0 0;
    font-family: "Cormorant Garamond", serif;
    font-size: 24px;
    letter-spacing: 1px;
  }
  .label--cream .style { color: var(--gold-deep); }
  .label--night .style { color: var(--pearl); }
  .method {
    margin: 34px 0 0;
    font-family: "Cinzel", serif;
    font-size: 12px;
    letter-spacing: 3px;
  }
  .brand {
    margin: 4px 0 0;
    font-family: "Cinzel", serif;
    font-size: 25px;
    letter-spacing: 4px;
  }
  .vintage, .region {
    margin: 4px 0 0;
    font-family: "Cinzel", serif;
    font-size: 11px;
    letter-spacing: 3px;
  }
  .label--cream .method,
  .label--cream .vintage,
  .label--cream .region { color: var(--ink-soft); }
  .label--cream .brand { color: var(--gold-deep); }
  .label--night .method,
  .label--night .vintage,
  .label--night .region,
  .label--night .brand { color: var(--pearl); }
</style>
</head>
<body>
  <main class="canvas">
    <section class="label label--cream">
      <div class="sparkle-art" role="img" aria-label="Champagne flute with an arc of rising bubbles and sparkles"></div>
      <h1 class="product-name">
        <span class="product-name__lead">Every Moonlit</span>
        <span class="product-name__main">Hour</span>
      </h1>
      <p class="style">Blanc de Blancs</p>
      <p class="method">Methode Traditionelle</p>
      <p class="brand">Beyond the Orchards</p>
      <p class="vintage">2015</p>
      <p class="region">Adelaide Hills</p>
    </section>

    <section class="label label--night">
      <div class="sparkle-art" role="img" aria-label="Champagne flute with an arc of rising bubbles and sparkles"></div>
      <h2 class="product-name">
        <span class="product-name__lead">Every Moonlit</span>
        <span class="product-name__main">Hour</span>
      </h2>
      <p class="style">Blanc de Blancs</p>
      <p class="method">Methode Traditionelle</p>
      <p class="brand">Beyond the Orchards</p>
      <p class="vintage">2015</p>
      <p class="region">Adelaide Hills</p>
    </section>
  </main>
</body>
</html>
```